Banner Ad Design Project for Muslim Fashion Site

I need banner ads for an e-commerce site selling modern muslim fashion, called "Selvarina.com". It is a flash sale site selling top designer brands of muslim fashion. The key driver of purchase is accessing special sale events for members, which goes up to 90% discount on certain brands.

We would like our logo "selvarina.com" to be part of the visual. You can get this logo on the top right of our site landing page (selvarina.com). The main visual should show an attractive lady with a modern looking hijab, if possible, with eye contact to the user, but not mandatory.

I am looking at very minimum 5 types of banner ad sizes:
728 x 90
120 x 600
300x 250
234 x 60
125 x125

3 concept variations are required.

Target Market(s)

asian modern muslim woman

Industry/Entity Type

E-Commerce

Requirements
Must have
• selvarina.com logo
attractive woman wearing modern looking hijab
the number "90%" to represent the discount on offer
the word "click here" as a call to action

```html
<!DOCTYPE html>
<html lang="en">
<head>
<meta charset="utf-8">
<title>Selvarina.com Banner Set</title>
<link href="https://fonts.googleapis.com/css2?family=Varela+Round&display=swap" rel="stylesheet">
<style>
  :root {
    --pink: #d42a8e;
    --pink-soft: #c9297f;
    --teal: #6ac3b6;
    --teal-edge: #58b0a4;
    --ink: #1d1b1c;
    --paper: #f4f4f4;
    --strip: #f1eeee;
    --white: #ffffff;
    --stone: #c8aa92;
    --scarf: #4d2231;
  }
  * { box-sizing: border-box; margin: 0; padding: 0; }
  html, body {
    width: 1200px; height: 900px; overflow: hidden;
    background: radial-gradient(ellipse at 50% 50%, #ffffff 0%, var(--paper) 70%);
    font-family: "Varela Round", "Helvetica Neue", Arial, sans-serif;
  }
  .stage {
    position: absolute; left: 0; top: 0;
    width: 1024px; height: 768px;
    transform: scale(1.171875); transform-origin: 0 0;
  }
  .banner { position: absolute; overflow: hidden; }
  .block { position: absolute; }
  .photo {
    position: absolute;
    background: linear-gradient(100deg, var(--stone) 0%, #b79580 30%, var(--scarf) 55%, #6a3a40 70%, var(--stone) 100%);
  }
  .photo--tall {
    background: linear-gradient(180deg, var(--scarf) 0%, #7a4a48 35%, #a87a64 50%, var(--scarf) 80%, #3d1b27 100%);
  }
  .photo--wide {
    background: linear-gradient(90deg, #d8c0ae 0%, #b28e7c 35%, var(--scarf) 60%, #8a5a4c 80%, #5a2a32 100%);
  }
  .band--pink { background: var(--pink); color: var(--white); }
  .band--ink { background: var(--ink); }
  .band--strip { background: var(--strip); }
  .headline {
    display: flex; align-items: center; justify-content: center;
    font-size: 19px; letter-spacing: -0.2px; white-space: nowrap;
  }
  .cta {
    position: absolute;
    background: var(--teal);
    border: 1px solid var(--teal-edge);
    color: var(--white);
    display: flex; align-items: center; justify-content: center;
    font-size: 18px; white-space: nowrap;
  }
  .brand {
    position: absolute;
    display: flex; align-items: center; justify-content: center; gap: 4px;
    color: var(--teal); white-space: nowrap;
  }
  .brand__dot {
    width: 7px; height: 7px; border-radius: 50%; background: var(--pink); flex: none;
  }
</style>
</head>
<body>
<main class="stage">

  <!-- 300 x 250, light footer -->
  <section class="banner" style="left:64px;top:15px;width:300px;height:250px;">
    <div class="photo" role="img" aria-label="Woman in a plum hijab against a stone wall" style="left:0;top:46px;width:300px;height:159px;"></div>
    <div class="block band--pink headline" style="left:0;top:0;width:300px;height:46px;">Sales up to 90% Off everyday</div>
    <div class="block band--strip" style="left:0;top:205px;width:300px;height:45px;"></div>
    <div class="brand" style="left:10px;top:205px;width:130px;height:45px;font-size:15px;"><span class="brand__dot"></span>Selvarina.com</div>
    <div class="cta" style="left:154px;top:210px;width:139px;height:34px;">click here</div>
  </section>

  <!-- 125 x 125 -->
  <section class="banner" style="left:384px;top:15px;width:125px;height:125px;">
    <div class="photo" role="img" aria-label="Woman in a plum hijab against a stone wall" style="left:0;top:0;width:125px;height:98px;"></div>
    <div class="block band--ink" style="left:3px;top:0;width:63px;height:23px;"></div>
    <div class="brand" style="left:3px;top:0;width:63px;height:23px;font-size:8px;gap:2px;"><span class="brand__dot" style="width:4px;height:4px;"></span>Selvarina.com</div>
    <div class="block band--pink headline" style="left:3px;top:23px;width:63px;height:26px;font-size:13px;">90% Off</div>
    <div class="cta" style="left:0;top:98px;width:125px;height:27px;font-size:16px;border:none;">click here</div>
  </section>

  <!-- 234 x 60 -->
  <section class="banner" style="left:529px;top:80px;width:234px;height:60px;">
    <div class="photo photo--wide" role="img" aria-label="Woman in a plum hijab against a stone wall" style="left:62px;top:0;width:172px;height:60px;"></div>
    <div class="block band--ink" style="left:0;top:0;width:62px;height:30px;"></div>
    <div class="brand" style="left:0;top:0;width:62px;height:30px;font-size:8px;gap:2px;"><span class="brand__dot" style="width:4px;height:4px;"></span>Selvarina.com</div>
    <div class="block band--pink headline" style="left:0;top:30px;width:62px;height:30px;font-size:13px;">90% Off</div>
  </section>

  <!-- 728 x 90, close crop -->
  <section class="banner" style="left:64px;top:282px;width:728px;height:90px;">
    <div class="photo photo--wide" role="img" aria-label="Close crop of a woman's eyes framed by a plum hijab" style="left:0;top:0;width:728px;height:90px;"></div>
    <div class="block band--strip" style="left:0;top:0;width:125px;height:46px;"></div>
    <div class="brand" style="left:0;top:0;width:125px;height:46px;font-size:15px;"><span class="brand__dot"></span>Selvarina.com</div>
    <div class="block band--pink headline" style="left:125px;top:0;width:300px;height:46px;">Sales up to 90% Off everyday</div>
    <div class="cta" style="left:285px;top:50px;width:140px;height:36px;">click here</div>
  </section>

  <!-- 728 x 90, dark logo -->
  <section class="banner" style="left:64px;top:390px;width:728px;height:90px;">
    <div class="block band--ink" style="left:0;top:0;width:125px;height:90px;"></div>
    <div class="brand" style="left:0;top:0;width:125px;height:90px;font-size:15px;"><span class="brand__dot"></span>Selvarina.com</div>
    <div class="photo" role="img" aria-label="Woman in a plum hijab against a stone wall" style="left:125px;top:0;width:354px;height:90px;"></div>
    <div class="block band--pink" style="left:479px;top:0;width:249px;height:90px;"></div>
    <div class="block headline" style="left:479px;top:14px;width:249px;height:26px;color:var(--white);font-size:17px;">Sales up to 90% Off everyday</div>
    <div class="cta" style="left:532px;top:47px;width:140px;height:36px;">click here</div>
  </section>

  <!-- 300 x 250, dark footer -->
  <section class="banner" style="left:64px;top:495px;width:300px;height:250px;">
    <div class="photo" role="img" aria-label="Woman in a plum hijab against a stone wall" style="left:0;top:46px;width:300px;height:159px;"></div>
    <div class="block band--pink headline" style="left:0;top:0;width:300px;height:46px;">Sales up to 90% Off everyday</div>
    <div class="block band--ink" style="left:0;top:205px;width:300px;height:45px;"></div>
    <div class="brand" style="left:10px;top:205px;width:130px;height:45px;font-size:15px;"><span class="brand__dot"></span>Selvarina.com</div>
    <div class="cta" style="left:154px;top:210px;width:139px;height:34px;">click here</div>
  </section>

  <!-- 120 x 600 -->
  <section class="banner" style="left:811px;top:51px;width:120px;height:600px;">
    <div class="block band--ink" style="left:0;top:0;width:120px;height:64px;"></div>
    <div class="brand" style="left:0;top:0;width:120px;height:64px;font-size:14px;"><span class="brand__dot"></span>Selvarina.com</div>
    <div class="photo photo--tall" role="img" aria-label="Woman in a plum hijab looking at the viewer" style="left:0;top:64px;width:120px;height:397px;"></div>
    <div class="block band--pink" style="left:0;top:461px;width:120px;height:139px;"></div>
    <div class="block" style="left:0;top:477px;width:120px;color:var(--white);font-size:23px;line-height:28px;text-align:center;">90% Off<br>Everyday</div>
    <div class="cta" style="left:4px;top:550px;width:112px;height:42px;">click here</div>
  </section>

</main>
</body>
</html>
```